Brisk Tutorium Website

We are looking for a new design of our website. The current website is www.brisktutorium.example. The company is the #1 pre-college math and science program in Orange County, CA. We would like to see designs that integrate our logo with a modern color scheme. We are also open for suggestions that could improve our logo. We would like a simple, minimal, clean, classy, and vibrant front-page user interface design that give the premium, modern, innovative, creative, and premier brand feel. We like the "New Retro Colors for the Web" as described here: http://www.pixel-layoutnook.example/en/layout-notes-2013/.

Target Market(s)

The target market is parents with K-12 students from a diverse population. Parents are well educated with family income > $150,000. Most of the decision makers are mothers from immigrate families: 30% Chinese, 30% Korean, 15% Indian, 24% White.

Industry/Entity Type

College

Requirements
Must have
• Must read our statement of differentiation at:
• http://brisktutorium.example/about-us
• Your design must be reflective of your understanding of the statements.
Nice to have
• The design should also be mobil friendly.
Should not have
• While most of our current classes are math, our company is expanding to include STEM (Science, Technology, Engineering, and Math) for gifted students. Therefore, the site should not be JUST a math education site.

```html
<!DOCTYPE html>
<html lang="en">
<head>
<meta charset="utf-8">
<title>Brisk Tutorium for Gifted Youth</title>
<link href="https://fonts.googleapis.com/css2?family=Arimo:wght@400;700&family=Noto+Serif:ital,wght@0,400;1,400&display=swap" rel="stylesheet">
<style>
:root{
  --green:#6ab04c;
  --green-dark:#4e8f36;
  --navy:#0c0c74;
  --title:#17178a;
  --text:#555;
  --grey:#d9d9d9;
  --white:#fff;
}
*{box-sizing:border-box;margin:0;padding:0}
html,body{width:986px;height:1200px;overflow:hidden;background:var(--white);font-family:"Arimo",Arial,sans-serif;color:var(--text)}
.page{position:relative;width:986px;height:1200px}
.abs{position:absolute}
/* header */
.brand{left:124px;top:22px;display:flex;align-items:center;gap:10px}
.brand-mark{width:34px;height:34px;background:var(--green)}
.brand-name{font-family:"Arimo",Arial,sans-serif;font-weight:400;font-size:24px;color:var(--navy);line-height:1}
.util{left:636px;top:9px;font-size:9px;color:#888}
.util span{margin:0 4px}
.login{left:808px;top:4px;width:54px;height:20px;background:var(--green);color:#fff;font-size:12px;text-align:center;line-height:20px}
.search-field{left:662px;top:47px;width:137px;height:20px;border:1px solid #ccc}
.search-btn{left:803px;top:47px;width:59px;height:20px;background:var(--navy);color:#fff;font-size:12px;text-align:center;line-height:20px}
.nav{left:0;top:82px;width:986px;height:30px;background:var(--green)}
.nav ul{position:absolute;left:124px;top:0;height:30px;display:flex;list-style:none;border-left:1px solid #fff}
.nav li{height:30px;line-height:30px;color:#fff;font-size:12px;border-right:1px solid #fff;text-align:center}
/* hero */
.hero{left:0;top:112px;width:986px;height:334px;background:linear-gradient(100deg,#4a5a60 0%,#c7a25a 22%,#7d5a48 45%,#8e6a8a 65%,#d4a77e 82%,#2d7f8e 100%)}
.caption{left:124px;top:384px;width:738px;height:62px;background:rgba(70,70,70,.78);color:#fff}
.caption h2{position:absolute;left:14px;top:8px;font-size:13.5px;font-weight:400}
.caption p{position:absolute;left:15px;top:29px;width:500px;font-size:10.5px;line-height:12.5px}
.dots{position:absolute;right:15px;top:29px;display:flex;gap:6px}
.dots span{width:17px;height:17px;background:var(--green);color:#fff;font-size:10px;font-weight:700;text-align:center;line-height:17px}
.dots .on{background:#fff;color:var(--green)}
/* main */
h1,.h2{font-family:"Noto Serif",serif;font-weight:400;color:var(--title)}
h1{left:124px;top:464px;font-size:18.5px}
.intro{left:124px;top:497px;width:516px;font-size:10.5px;line-height:13px;text-align:justify;letter-spacing:.2px}
.intro p{margin-bottom:13px}
.courses{left:124px;top:677px;display:flex;gap:18px}
.course{width:115px;height:62px;background:var(--green);color:#fff;font-weight:700;font-size:14px;text-align:center;display:flex;align-items:center;justify-content:center;line-height:16px}
.h2{left:124px;top:766px;font-size:18.5px}
.avatar{left:128px;top:802px;width:104px;height:104px;border-radius:50%;background:radial-gradient(circle at 50% 45%,#9a8670,#3e4a3a);border:3px solid #eee}
.quote-mark{left:240px;top:804px;font-family:"Noto Serif",serif;font-size:40px;color:var(--green);line-height:1}
.quote{left:246px;top:817px;width:394px;font-family:"Noto Serif",serif;font-style:italic;font-size:14px;line-height:15px;color:#444}
.author{left:540px;top:875px;width:100px;text-align:right;font-family:"Noto Serif",serif;font-size:14px;color:var(--title)}
/* calendar */
.cal{left:693px;top:468px;width:169px}
.cal-head{height:22px;background:var(--green);display:flex;color:#fff;font-size:11px}
.cal-head .arr{width:24px;text-align:center;line-height:22px;background:var(--green-dark)}
.cal-head .m{flex:1;text-align:center;line-height:22px}
.cal-days,.cal-grid{display:grid;grid-template-columns:repeat(7,1fr)}
.cal-days{background:var(--green);color:#fff;font-size:6.5px;height:15px;line-height:15px;text-align:center}
.cal-grid div{height:24px;line-height:24px;text-align:center;font-size:10px;color:#333;background:#e2e2e2;border-right:1px solid #fff;border-bottom:1px solid #fff}
.cal-grid .today{color:var(--green-dark);font-weight:700}
.cal-grid .mute{color:#aaa}
/* news */
.tabs{left:693px;top:650px;width:169px;height:28px;display:flex}
.tabs div{flex:1;text-align:center;line-height:28px;font-size:13.5px;color:#fff;background:var(--green)}
.tabs .active{background:var(--green-dark)}
.news{left:693px;top:678px;width:169px;height:237px;background:#e8e8e8;padding:4px 6px}
.news-inner{background:#fff;height:100%;padding:6px 8px}
.item{padding:4px 0 6px;border-bottom:1px dotted #bbb;margin-bottom:4px}
.item:last-child{border:0}
.item h3{font-size:9.5px;color:var(--navy)}
.item time{display:block;font-size:8.5px;font-style:italic;color:#999;margin:2px 0}
.item p{font-size:9px;line-height:11px;text-align:justify;letter-spacing:.3px}
/* subscribe */
.band{left:0;top:958px;width:986px;height:53px;background:var(--navy)}
.band p{position:absolute;left:124px;top:15px;font-size:17px;color:#fff}
.email{position:absolute;left:477px;top:12px;width:209px;height:30px;background:#fff;border-radius:3px;font-size:13.5px;color:#888;line-height:30px;padding-left:10px}
.subscribe{position:absolute;left:693px;top:12px;width:169px;height:30px;background:#2a2a8c;border-radius:3px;color:#fff;font-weight:700;font-size:13px;text-align:center;line-height:30px}
/* footer */
.footer{left:0;top:1011px;width:986px;height:162px;background:var(--grey)}
.col{position:absolute;top:24px;font-size:9px;font-weight:400;line-height:11px;letter-spacing:.4px;color:#666}
.col h4{font-size:13.5px;font-weight:400;color:var(--navy);margin-bottom:15px;letter-spacing:0}
.col p{margin-bottom:11px}
.col li{list-style:none;margin-bottom:7.5px}
.contact li{display:flex;gap:8px;margin-bottom:11px}
.social{display:flex;gap:12px;margin-top:10px}
.social span{width:26px;height:26px;border-radius:50%;border:2px solid #888}
.bottom{left:0;top:1173px;width:986px;height:27px;background:#c4c4c4;font-size:9.5px;color:#333}
.bottom p{position:absolute;left:124px;top:8px}
.top-btn{position:absolute;left:841px;top:-6px;width:21px;height:21px;background:#555;border-radius:3px}
</style>
</head>
<body>
<div class="page">
  <header>
    <div class="abs brand"><span class="brand-mark"></span><span class="brand-name">Brisk Tutorium</span></div>
    <div class="abs util">Blog<span>|</span>Jobs<span>|</span>Site Map<span>|</span>Accessibility</div>
    <div class="abs login">Login</div>
    <div class="abs search-field"></div>
    <div class="abs search-btn">Search</div>
  </header>
  <nav class="abs nav"><ul>
    <li style="width:65px">Home</li><li style="width:77px">About Us</li><li style="width:85px">Admission</li><li style="width:88px">Academics</li><li style="width:74px">Courses</li><li style="width:106px">News / Events</li><li style="width:69px">Results</li><li style="width:80px">Fall 2013</li><li style="width:92px">Contact Us</li>
  </ul></nav>

  <div class="abs hero" role="img" aria-label="Photo of smiling students in a classroom"></div>
  <div class="abs caption">
    <h2>Lorem ipsum dolor sit amet, consectetur adipiscing elit</h2>
    <p>Vestibulum faucibus augue at purus iaculis pulvinar. Phasellus at urna sagittis, facilisis quam et, pharetra augue. Vestibulum ante ipsum primis in faucibus orci</p>
    <div class="dots"><span>1</span><span class="on">2</span><span>3</span><span>4</span><span>5</span></div>
  </div>

  <h1 class="abs">Welcome to Brisk Tutorium For Gifted Youth</h1>
  <div class="abs intro">
    <p>Lorem ipsum dolor sit amet, consectetur adipiscing elit. Nulla eu porta lorem. Cras turpis ipsum, iaculis ut auctor eget, euismod eget enim. Curabitur a lorem porttitor lectus euismod semper vitae eu purus.</p>
    <p>Lorem ipsum dolor sit amet, consectetur adipiscing elit. Nulla eu porta lorem. Cras turpis ipsum, iaculis ut auctor eget, euismod eget enim. Curabitur a lorem porttitor lectus euismod semper vitae eu purus. Nulla at mi scelerisque urna dapibus ornare. Vestibulum ante ipsum primis in faucibus orci luctus et ultrices posuere cubilia Curae; Aliquam nec lectus elit, at aliquam est. Proin eget laoreet lectus.</p>
    <p>Nullam scelerisque cursus leo at volutpat. Etiam non faucibus ante. Ut eget leo placerat velit imperdiet suscipit. , at aliquam est. Proin eget laoreet lectus. Nullam scelerisque cursus leo at volutpat. Etiam non faucibus ante. Ut eget leo placerat velit imperdiet suscipit. at aliquam est. Proin eget laoreet lectus. Nullam scelerisque cursus leo at volutpat.</p>
  </div>
  <div class="abs courses">
    <div class="course">SCIENCE<br>COURSES</div>
    <div class="course">TECHNOLOGY<br>COURSES</div>
    <div class="course">ENGINEERING<br>COURSES</div>
    <div class="course">MATH<br>COURSES</div>
  </div>

  <div class="abs h2">What Students say’s</div>
  <div class="abs avatar" role="img" aria-label="Portrait photo of student"></div>
  <div class="abs quote-mark">“</div>
  <p class="abs quote">&nbsp;&nbsp;&nbsp;Curabitur blandit tempus porttitor. Integer posuere erat a ante venenatis dapibus posuere velit aliquet. Nulla vitae elit libero, a pharetra augue.Cras mattis consectetur.</p>
  <div class="abs author">John Ipsum</div>

  <aside class="abs cal">
    <div class="cal-head"><span class="arr">‹</span><span class="m">JANUARY</span><span class="arr">›</span></div>
    <div class="cal-days"><span>SUN</span><span>MON</span><span>TUE</span><span>WED</span><span>THU</span><span>FRI</span><span>SAT</span></div>
    <div class="cal-grid">
      <div>1</div><div>2</div><div>3</div><div>4</div><div>5</div><div>6</div><div>7</div>
      <div>8</div><div>9</div><div>10</div><div>11</div><div>12</div><div>13</div><div>14</div>
      <div>15</div><div>16</div><div>17</div><div>18</div><div>19</div><div class="today">20</div><div>21</div>
      <div>22</div><div>23</div><div>24</div><div>25</div><div>26</div><div>27</div><div>28</div>
      <div>29</div><div>30</div><div>31</div><div class="mute">1</div><div class="mute">2</div><div class="mute">3</div><div class="mute">4</div>
    </div>
  </aside>

  <div class="abs tabs"><div class="active">NEWS</div><div>EVENTS</div></div>
  <div class="abs news"><div class="news-inner">
    <div class="item"><h3>Lorem ipsum dolor sit amet</h3><time>2013-06-02</time><p>Lorem ipsum dolor sit amet, consectetur adipiscing elit. Pellentesque eget.</p></div>
    <div class="item"><h3>Lorem ipsum dolor sit amet</h3><time>2013-06-02</time><p>Lorem ipsum dolor sit amet, consectetur adipiscing elit. Pellentesque eget.</p></div>
    <div class="item"><h3>Lorem ipsum dolor sit amet</h3><time>2013-06-02</time><p>Lorem ipsum dolor sit amet, consectetur adipiscing elit. Pellentesque eget.</p></div>
  </div></div>

  <section class="abs band">
    <p>Stay in touch by email for updates and offers</p>
    <div class="email">Your Email Here...</div>
    <div class="subscribe">SUBSCRIBE NOW</div>
  </section>

  <footer class="abs footer">
    <div class="col" style="left:124px;width:170px">
      <h4>About Us</h4>
      <p>Lorem ipsum dolor sit amet, consectetur adipiscing elit. Vivamus sit amet ligula vel diam congue semper.</p>
      <p>Ligula vel diam congue semper.Lorem ipsum dolor sit amet, consectetur adipiscing elit. Vivamus</p>
    </div>
    <div class="col" style="left:330px;width:140px">
      <h4>Courses Offer</h4>
      <ul><li>›&nbsp; Science Courses</li><li>›&nbsp; Technolgy Courses</li><li>›&nbsp; Engineering Courses</li><li>›&nbsp; Math Courses</li></ul>
    </div>
    <div class="col contact" style="left:488px;width:180px">
      <h4>Contact Us</h4>
      <ul>
        <li><svg width="12" height="11" viewBox="0 0 12 11"><path d="M6 0 0 5h2v6h3V7h2v4h3V5h2z" fill="#888"/></svg><span>88 Scholar Lane, Suite 140<br>Lakeview, CA 90000-0000</span></li>
        <li><svg width="12" height="11" viewBox="0 0 12 11"><path d="M2 0h3l1 3-2 1q1 3 3 4l1-2 3 1v3q-6 0-9-6z" fill="#888"/></svg><span>(555) 010-2468</span></li>
        <li><svg width="12" height="11" viewBox="0 0 12 11"><rect y="2" width="12" height="8" fill="#888"/><path d="M0 2l6 4 6-4" stroke="#fff" fill="none"/></svg><span>info@brisktutorium.example</span></li>
      </ul>
    </div>
    <div class="col" style="left:693px;width:170px">
      <h4>Stay In Touch</h4>
      <p>Follow US in our social networks! Lorem ipsum dolor sit amet, consectetur and go adipiscing elit.</p>
      <div class="social"><span></span><span></span><span></span></div>
    </div>
  </footer>
  <div class="abs bottom">
    <p>Copyright © 2000-2013 , Brisk Tutorium for Gifted Youth.</p>
    <div class="top-btn"><svg width="21" height="21" viewBox="0 0 21 21"><path d="M6 13l4.5-5 4.5 5" stroke="#fff" stroke-width="2.5" fill="none"/></svg></div>
  </div>
</div>
</body>
</html>
```